Website design for online service business

The company provides the following services:
1 - consultancy services on existing products (like tallydesk and brisk 354)
2 - Coaching services - Coach someone on services like using/developing features with existing products, or teach how to be more productive, or improve their business using automation, etc
3 - Training
- Online training on demand on existing products via vokra (like in Tallydesk and brisk 365)
- Online courses through videos lessons and scripts by offering information products where people will need to register and pay in advance to access the online course. (productivity courses for example)

- The goal is for clients to book time with me for one of those areas without too many clicks.
- Clients will be able to Book time using an integration (it would be good to have the layout integrated with the site.) with this https://planner.brisk-suite.example/owa/calendar/BrightKelpStudio1@brightkelpstudio.bookhub.example/bookings/

- there will be areas for which i whish to build a VIP mailing list. It's referenced on the wireframes

References:
https://www.lanternfieldnotes.example/about/about-dorvan/
https://www.pebblecompass.example/
https://tallydeskguide.example/

Target Market(s)

- Small businesses
- Freelancers

Industry/Entity Type

Business

Number of Pages Required

5+ page

Font styles to use
Sans Serif

Colors

Designer to choose colors to be used in the design.

Requirements
Must have
• Must have the design optimized to the less clicks possible to achieve any action
• The colors of the site should follow the logo (provided in attach)
• It should use other color that belong to the same pallet of colors
• Should contain colors that incentivizes people to click and book something
• Images and backgrounds should be made available
• All images sizes and colors should be provided to be able to develop the site according to the design
Nice to have
• The bookings for the time should be integrated within the design. If not possible a redirection to it can work as well.
Should not have
• Links to social media
• Pop-ups
• Intrusive navigations (like navigation bares on the left or right hand side)
• Should not be a template used by many people

```html
<!DOCTYPE html>
<html lang="en">
<head>
<meta charset="utf-8">
<title>Bright Kelp — Consulting, Coaching &amp; Training</title>
<link href="https://fonts.googleapis.com/css2?family=Poppins:wght@300;400;500;600;700&family=Rajdhani:wght@600;700&display=swap" rel="stylesheet">
<style>
:root{
  --navy:#123a66;
  --navy-deep:#0c2747;
  --orange:#f7941d;
  --orange-dark:#e9800c;
  --ink:#2b2b2b;
  --muted:#5d6470;
  --light:#f2f3f5;
  --footer:#0f1b2b;
  --footer-bar:#0a1420;
  --white:#ffffff;
}
*{box-sizing:border-box;margin:0;padding:0}
html,body{width:1200px;height:2678px;overflow:hidden}
body{position:relative;font-family:'Poppins',sans-serif;color:var(--ink);background:var(--white)}
.abs{position:absolute}

/* hero */
.hero{left:0;top:0;width:1200px;height:575px;background:linear-gradient(120deg,#1c4c80 0%,#153f6d 45%,#21507f 70%,#183f68 100%)}
.hero-shade{left:0;top:0;width:1200px;height:575px;background:linear-gradient(90deg,rgba(12,39,71,.75) 0%,rgba(12,39,71,.35) 55%,rgba(12,39,71,.1) 100%)}
.logo{left:132px;top:22px;width:110px;text-align:center;color:var(--white)}
.logo-mark{width:22px;height:22px;background:var(--white);margin:0 auto 4px}
.logo-name{font-family:'Poppins',sans-serif;font-weight:600;font-size:14px;letter-spacing:1.5px;line-height:1.1}
.nav-item{top:57px;font-size:10.5px;font-weight:600;color:var(--white);white-space:nowrap;line-height:14px}
.nav-rule{left:405px;top:0;width:2px;height:44px;background:var(--orange)}
.btn{display:inline-flex;align-items:center;justify-content:center;border-radius:20px;font-weight:600;font-size:11.5px;letter-spacing:.3px;white-space:nowrap}
.btn-orange{background:var(--orange);color:var(--white)}
.btn-ghost{border:2px solid var(--white);color:var(--white)}
.nav-cta{left:901px;top:46px;width:166px;height:32px;font-size:11px}
.hero-kicker{left:159px;top:199px;font-size:15px;line-height:20px;font-weight:600;color:var(--white);letter-spacing:.3px}
.hero-title{left:157px;top:222px;font-family:'Rajdhani',sans-serif;font-weight:700;font-size:34px;line-height:35px;color:var(--orange);white-space:nowrap}
.hero-copy{left:159px;top:297px;width:540px;font-size:11.5px;line-height:22px;color:#e4ebf3}
.hero-btn1{left:159px;top:358px;width:118px;height:32px}
.hero-btn2{left:290px;top:358px;width:116px;height:32px}
.dots{left:172px;top:416px;display:flex;gap:16px}
.dot{width:8px;height:8px;border-radius:50%;background:#c9d3de}
.dot.on{background:var(--orange)}
.side-arrow{top:282px;width:36px;height:36px;border-radius:50%;background:var(--orange)}
.side-arrow.l{left:-18px}.side-arrow.r{left:1182px}

/* service cards */
.card{top:505px;height:185px;border:4px solid var(--white);box-shadow:0 4px 14px rgba(0,0,0,.15)}
.card-photo{width:100%;height:100%}
.card-icon{left:8px;bottom:8px;width:46px;height:46px;background:var(--orange)}
.card-label{font-size:11.5px;font-weight:600;text-align:center;line-height:17px;color:var(--ink)}
.coach-box{background:#2b3440}
.coach-text{left:30px;top:16px;width:245px;font-size:11px;line-height:18px;color:#e6e6e6}
.read-more{right:22px;bottom:18px;font-size:11px;font-weight:600;color:var(--orange)}
.deco-ring{left:1045px;top:540px;width:230px;height:230px;border-radius:26px;background:rgba(18,58,102,.07);transform:rotate(18deg)}
.deco-dot{left:905px;top:745px;width:80px;height:80px;border-radius:50%;background:rgba(247,148,29,.14)}
.divider{left:133px;top:773px;width:935px;height:1px;background:#e5e7ea}

/* welcome */
.eyebrow{font-size:12px;font-weight:500;color:var(--orange)}
.h2{font-size:21px;font-weight:600;color:var(--ink)}
.body{font-size:11.5px;line-height:25px;color:var(--muted)}
.welcome-photo{left:612px;top:826px;width:458px;height:287px;background:linear-gradient(135deg,#eef1f4 0%,#c9d4de 55%,#9fb1c1 100%)}

/* booking */
.booking{left:0;top:1167px;width:1200px;height:488px;background:linear-gradient(100deg,#2f3338 0%,#4a4e54 45%,#3a3d42 100%)}
.booking-shade{left:0;top:1167px;width:1200px;height:488px;background:rgba(20,22,26,.45)}
.booking-intro{left:153px;top:1232px;font-size:20px;font-weight:300;color:var(--white)}
.booking-title{left:153px;top:1258px;font-size:27px;font-weight:600;color:var(--orange)}
.booking-copy{left:157px;top:1310px;width:400px;font-size:11.5px;line-height:23px;color:#eceff2}
.booking-btn{left:153px;top:1560px;width:257px;height:40px;font-size:13px}
.laptop{left:560px;top:1273px}
.screen{left:28px;top:8px;width:434px;height:262px;background:var(--white);overflow:hidden}

/* team */
.team{left:0;top:1655px;width:1200px;height:720px;background:var(--light)}
.team-head{left:618px;top:1703px;font-size:14px;font-weight:700;color:var(--ink)}
.team-copy{left:618px;top:1733px;width:440px;font-size:11px;line-height:21px;color:var(--muted)}
.team-link{left:618px;top:1796px;font-size:11px;color:var(--orange)}
.avatar{border-radius:50%;background:linear-gradient(160deg,#d9dee4,#a7b2bf)}
.avatar.halo{box-shadow:0 0 0 10px rgba(247,148,29,.12)}
.member{width:160px;text-align:center}
.member b{display:block;font-size:11.5px;font-weight:600;color:var(--ink)}
.member span{font-size:9.5px;color:var(--muted)}

/* footer */
.footer{left:0;top:2375px;width:1200px;height:303px;background:var(--footer)}
.footer-bar{left:0;top:2630px;width:1200px;height:48px;background:var(--footer-bar)}
.f-head{font-size:11.5px;font-weight:600;color:var(--white);letter-spacing:.4px}
.f-line{width:28px;height:2px;background:var(--orange);margin-top:6px}
.f-list{list-style:none;font-size:10.5px;color:#c7ced8}
.f-list li{display:flex;gap:12px;align-items:flex-start;line-height:17px;margin-bottom:8px}
.f-ico{flex:0 0 10px;height:10px;margin-top:3px}
.f-text{font-size:10.5px;line-height:18px;color:#c7ced8}
.news-input{width:190px;height:32px;border:1px solid #3b4656;font-size:10px;color:#7d8896;padding:9px 10px}
.news-btn{width:80px;height:24px;background:var(--orange);color:var(--white);font-size:10px;display:flex;align-items:center;justify-content:center}
.copyright{left:133px;top:2652px;font-size:9px;color:#8b95a3}
.socials{left:925px;top:2647px;display:flex;gap:10px}
.social{width:16px;height:16px;background:#2d6fb8}
</style>
</head>
<body>

<!-- HERO -->
<div class="abs hero" role="img" aria-label="Hero photo: hands typing on a laptop at a desk, tinted deep blue"></div>
<div class="abs hero-shade"></div>

<div class="abs logo"><div class="logo-mark"></div><div class="logo-name">BRIGHT KELP</div></div>
<div class="abs nav-rule"></div>
<nav>
  <span class="abs nav-item" style="left:386px">HOME</span>
  <span class="abs nav-item" style="left:446px">SERVICES</span>
  <span class="abs nav-item" style="left:526px">TRAINING</span>
  <span class="abs nav-item" style="left:605px">CLIENTS</span>
  <span class="abs nav-item" style="left:677px">BLOG</span>
  <span class="abs nav-item" style="left:734px">ABOUT US</span>
  <span class="abs nav-item" style="left:818px">CONTACT US</span>
</nav>
<div class="abs btn btn-orange nav-cta">BOOK AN APPOINTMENT</div>

<div class="abs hero-kicker">CORVANE TALLYDESK</div>
<h1 class="abs hero-title">SERVER 2013 TRAINING<br>SESSION 2018 - 2019</h1>
<p class="abs hero-copy">Lorem ipsum dolor sit amet, consectetuer adipiscing elit. Aenean commodo ligula eget dolor. Aenean massa. Cum sociis natoque penatibus et magnis dis parturient montes,</p>
<div class="abs btn btn-ghost hero-btn1">VIEW MORE</div>
<div class="abs btn btn-orange hero-btn2">GET INSPIRED</div>
<div class="abs dots"><span class="dot"></span><span class="dot"></span><span class="dot on"></span><span class="dot"></span></div>
<div class="abs side-arrow l"></div>
<div class="abs side-arrow r"></div>

<!-- SERVICES -->
<div class="abs deco-ring"></div>
<div class="abs deco-dot"></div>

<div class="abs card" style="left:133px;width:277px">
  <div class="card-photo" role="img" aria-label="Photo: laptop with app tiles beside a coffee mug on a wooden desk" style="background:linear-gradient(135deg,#c9a27a,#8a6a4d 60%,#5b4636)"></div>
  <div class="abs card-icon"></div>
</div>
<div class="abs card coach-box" style="left:445px;width:305px">
  <div class="card-photo" role="img" aria-label="Dark photo backdrop of a coaching session" style="background:linear-gradient(135deg,#3a4350,#262d36)"></div>
  <p class="abs coach-text">Coach someone on services like using/developing features with existing products, or teach how to be more productive, or improve their business using automation, etc</p>
  <div class="abs card-icon"></div>
  <div class="abs read-more">READ MORE &raquo;</div>
</div>
<div class="abs card" style="left:790px;width:277px">
  <div class="card-photo" role="img" aria-label="Photo: audience seated in a bright training room" style="background:linear-gradient(135deg,#eef0f2,#c4ccd4 60%,#9aa6b2)"></div>
  <div class="abs card-icon"></div>
</div>

<div class="abs card-label" style="left:133px;top:703px;width:277px">CONSULTANCY SERVICES ON<br>EXISTING PRODUCTS</div>
<div class="abs card-label" style="left:445px;top:705px;width:305px">COACHING SERVICES</div>
<div class="abs card-label" style="left:790px;top:703px;width:277px">TRAINING</div>

<div class="abs divider"></div>

<!-- WELCOME -->
<div class="abs eyebrow" style="left:133px;top:818px">Welcome To Us</div>
<h2 class="abs h2" style="left:133px;top:836px">Top Consulting Agency</h2>
<p class="abs body" style="left:135px;top:873px;width:455px">Must explain to you how all this mistaken idea denouncing plesure praising pain was born and I will give you a complete account of the system expound teachings the great explorer of the truth, the master-builder.</p>
<p class="abs body" style="left:135px;top:960px;width:455px">Who do not know how to pursue pleasure rationally encounter consequences that are extremely painful. Nor again is there anyone who loves or pursues or desires obtain pain of itself,</p>
<div class="abs btn btn-orange" style="left:133px;top:1070px;width:161px;height:34px;font-weight:500">Know more about us</div>
<div class="abs welcome-photo" role="img" aria-label="Photo: two colleagues working together at a laptop in a bright office"></div>

<!-- BOOKING -->
<div class="abs booking" role="img" aria-label="Background photo: team meeting around a table, darkened"></div>
<div class="abs booking-shade"></div>
<div class="abs booking-intro">Introducing the all-new BrightKelp</div>
<div class="abs booking-title">Online Booking System</div>
<p class="abs booking-copy">The new booking system will give you better access to online class bookins, Membership signups and renewals and much more.Must explain to you how all this mistaken idea denouncing plesure praising pain was born and I will give you a complete account of the system expound teachings the great explorer of the truth, the master-builder.<br><br>Who do not know how to pursue pleasure rationally encounter consequences that are extremely painful. Nor again is there anyone</p>
<div class="abs btn btn-orange booking-btn">CLICK HERE FOR BOOKING</div>

<div class="abs laptop">
  <svg width="505" height="290" viewBox="0 0 505 290">
    <rect x="18" y="0" width="470" height="278" rx="10" fill="#1d1f22"/>
    <rect x="0" y="276" width="505" height="12" rx="3" fill="#c9ccd0"/>
    <rect x="210" y="276" width="85" height="5" fill="#9ea3a9"/>
  </svg>
  <div class="abs screen">
    <svg width="434" height="262" viewBox="0 0 434 262" font-family="Poppins, sans-serif">
      <text x="217" y="14" font-size="6" fill="#444" text-anchor="middle">Our first class</text>
      <rect x="110" y="24" width="214" height="34" fill="#0f7b6c"/>
      <text x="118" y="36" font-size="5.5" fill="#fff">Our first class</text>
      <text x="118" y="45" font-size="4.5" fill="#d7efe9">Trainer</text>
      <text x="118" y="52" font-size="4.5" fill="#d7efe9">Live</text>
      <line x1="0" y1="76" x2="434" y2="76" stroke="#e3e3e3"/>
      <text x="217" y="88" font-size="6" fill="#444" text-anchor="middle">April 30</text>
      <text x="60" y="108" font-size="5" fill="#555">April 2018</text>
      <text x="230" y="108" font-size="5" fill="#555">Select staff (optional)</text>
      <rect x="230" y="113" width="130" height="11" fill="none" stroke="#ccc"/>
      <text x="236" y="121" font-size="4.5" fill="#777">Anyone</text>
      <g font-size="4.5" fill="#555">
        <text x="60" y="124">Su</text><text x="78" y="124">Mo</text><text x="96" y="124">Tu</text><text x="114" y="124">We</text><text x="132" y="124">Th</text><text x="150" y="124">Fr</text><text x="168" y="124">Sa</text>
      </g>
      <circle cx="62" cy="136" r="6" fill="#0f7b6c"/>
      <g font-size="4.5" fill="#666">
        <text x="60" y="138" fill="#fff">1</text><text x="78" y="138">2</text><text x="96" y="138">3</text><text x="114" y="138">4</text><text x="132" y="138">5</text><text x="150" y="138">6</text><text x="168" y="138">7</text>
        <text x="60" y="155">8</text><text x="78" y="155">9</text><text x="96" y="155">10</text><text x="114" y="155">11</text><text x="132" y="155">12</text><text x="150" y="155">13</text><text x="168" y="155">14</text>
        <text x="60" y="172">15</text><text x="78" y="172">16</text><text x="96" y="172">17</text><text x="114" y="172">18</text><text x="132" y="172">19</text><text x="150" y="172">20</text><text x="168" y="172">21</text>
        <text x="60" y="189">22</text><text x="78" y="189">23</text><text x="96" y="189">24</text><text x="114" y="189">25</text><text x="132" y="189">26</text><text x="150" y="189">27</text><text x="168" y="189">28</text>
        <text x="60" y="206">29</text><text x="78" y="206">30</text>
        <text x="230" y="142">1:00 pm</text><text x="265" y="142">1:30 pm</text><text x="300" y="142">2:00 pm</text>
        <text x="230" y="159">2:30 pm</text><text x="265" y="159">3:00 pm</text><text x="300" y="159">3:30 pm</text>
        <text x="230" y="176">4:00 pm</text><text x="265" y="176">4:30 pm</text><text x="300" y="176">5:00 pm</text>
        <text x="230" y="193">5:30 pm</text>
      </g>
    </svg>
  </div>
</div>

<!-- TEAM -->
<div class="abs team" role="img" aria-label="Soft light grey background with faint geometric shapes"></div>
<h3 class="abs team-head">OUR EXPERIENCED TEAM OF EXPERTS</h3>
<p class="abs team-copy">Our experienced team of data experts are passionate about turning the morass of unstructured data into actionable intelligence. The core team consists of regionally and globally experienced executives and technologycific needs.</p>
<div class="abs team-link">Meet Our Team &rarr;</div>

<div class="abs avatar" role="img" aria-label="Portrait photo of team member" style="left:155px;top:1767px;width:126px;height:126px"></div>
<div class="abs member" style="left:138px;top:1905px"><b>Arlo Venn</b><span>CEO &amp; Founder</span></div>

<div class="abs avatar halo" role="img" aria-label="Portrait photo of team member" style="left:403px;top:1812px;width:172px;height:172px"></div>
<div class="abs member" style="left:409px;top:1986px"><b>Mira Solace</b><span>CEO &amp; Founder</span></div>

<div class="abs avatar" role="img" aria-label="Portrait photo of team member" style="left:688px;top:1848px;width:126px;height:126px"></div>
<div class="abs member" style="left:671px;top:1986px"><b>Arlo Venn</b><span>CEO &amp; Founder</span></div>

<div class="abs avatar" role="img" aria-label="Portrait photo of team member" style="left:177px;top:2004px;width:126px;height:126px"></div>
<div class="abs member" style="left:160px;top:2143px"><b>Arlo Venn</b><span>CEO &amp; Founder</span></div>

<div class="abs avatar" role="img" aria-label="Portrait photo of team member" style="left:857px;top:1975px;width:160px;height:160px"></div>
<div class="abs member" style="left:857px;top:2145px"><b>Mira Solace</b><span>CEO &amp; Founder</span></div>

<div class="abs avatar" role="img" aria-label="Portrait photo of team member" style="left:579px;top:2065px;width:126px;height:126px"></div>
<div class="abs member" style="left:562px;top:2202px"><b>Arlo Venn</b><span>CEO &amp; Founder</span></div>

<div class="abs avatar" role="img" aria-label="Portrait photo of team member" style="left:305px;top:2180px;width:126px;height:126px"></div>
<div class="abs member" style="left:288px;top:2319px"><b>Arlo Venn</b><span>CEO &amp; Founder</span></div>

<!-- FOOTER -->
<div class="abs footer" role="img" aria-label="Dark navy footer with a faint world map"></div>

<div class="abs" style="left:138px;top:2420px">
  <div class="f-head">GLOBAL HQ</div><div class="f-line"></div>
  <ul class="f-list" style="margin-top:22px;width:210px">
    <li><svg class="f-ico" viewBox="0 0 10 10"><path d="M2 1l2 2-1 1.5c.8 1.4 1.7 2.2 3 3L7.5 6l2 2-1.5 1.5C4.5 9 1 5.5.5 2.5z" fill="#f7941d"/></svg>+1 (555) 014-2280</li>
    <li><svg class="f-ico" viewBox="0 0 10 10"><rect x="0" y="2" width="10" height="6.5" fill="#f7941d"/><path d="M0 2l5 3.5L10 2" stroke="#0f1b2b" fill="none"/></svg>hello.us@northwind-data.example</li>
    <li><svg class="f-ico" viewBox="0 0 10 10"><circle cx="5" cy="5" r="4.5" fill="#f7941d"/></svg>www.northwind-data.example</li>
    <li><svg class="f-ico" viewBox="0 0 10 10"><path d="M5 0a3.5 3.5 0 0 1 3.5 3.5C8.5 6 5 10 5 10S1.5 6 1.5 3.5A3.5 3.5 0 0 1 5 0z" fill="#f7941d"/></svg>418 Ember Lane, Suite 20,<br>Fairhaven, CA 90000, USA</li>
  </ul>
</div>

<div class="abs" style="left:375px;top:2420px">
  <div class="f-head">REGIONAL HQ</div><div class="f-line"></div>
  <ul class="f-list" style="margin-top:22px;width:215px">
    <li><svg class="f-ico" viewBox="0 0 10 10"><path d="M2 1l2 2-1 1.5c.8 1.4 1.7 2.2 3 3L7.5 6l2 2-1.5 1.5C4.5 9 1 5.5.5 2.5z" fill="#f7941d"/></svg>+65 5550 1142</li>
    <li><svg class="f-ico" viewBox="0 0 10 10"><rect x="0" y="2" width="10" height="6.5" fill="#f7941d"/><path d="M0 2l5 3.5L10 2" stroke="#0f1b2b" fill="none"/></svg>hello.sg@northwind-data.example</li>
    <li><svg class="f-ico" viewBox="0 0 10 10"><circle cx="5" cy="5" r="4.5" fill="#f7941d"/></svg>www.northwind-data.example</li>
    <li><svg class="f-ico" viewBox="0 0 10 10"><path d="M5 0a3.5 3.5 0 0 1 3.5 3.5C8.5 6 5 10 5 10S1.5 6 1.5 3.5A3.5 3.5 0 0 1 5 0z" fill="#f7941d"/></svg>12 Kestrel Road, #04-08<br>Harbour Hub, Singapore 400000</li>
  </ul>
</div>

<div class="abs" style="left:617px;top:2420px;width:200px">
  <div class="f-head">WORKING HOURS</div><div class="f-line"></div>
  <p class="f-text" style="margin-top:16px">We work weekdays. Please contact us for any enquiry</p>
  <p class="f-text" style="margin-top:10px;display:flex;gap:10px;align-items:center"><svg width="11" height="11" viewBox="0 0 11 11"><circle cx="5.5" cy="5.5" r="4.5" fill="none" stroke="#f7941d" stroke-width="1.4"/><path d="M5.5 3v2.7l2 1.2" stroke="#f7941d" fill="none" stroke-width="1.2"/></svg>Monday – Friday : 9AM – 6PM</p>
  <p class="f-text" style="margin-top:4px;padding-left:29px;color:var(--orange)">Weekends Holiday</p>
</div>

<div class="abs" style="left:850px;top:2420px;width:210px">
  <div class="f-head">NEWSLETTER</div><div class="f-line"></div>
  <p class="f-text" style="margin-top:16px">Subscribe to our newsletter for latest updates about our company</p>
  <div class="news-input" style="margin-top:14px">Your Email address</div>
  <div class="news-btn" style="margin-top:14px">SUBSCRIBE</div>
</div>

<div class="abs footer-bar"></div>
<div class="abs copyright">Copyright © 2018 - 2019 brightkelp.example. All Rights Reserved.</div>
<div class="abs socials"><span class="social"></span><span class="social"></span><span class="social"></span><span class="social" style="background:#d23b2e"></span><span class="social" style="background:#f7941d"></span></div>

</body>
</html>
```